Nail salon window signage design

We need new signage to be designed for our existing nail salon. The sign will be a large sticker that will stick onto the glass window at the front.

Some of the services we provide are:
Manicures
Pedicures
Velora Gel Builder
Acrylic Nails
KVT
Brenlux
Gel Polish
You may wish to have our services listed on the sign but is not compulsory.

I have also attached our logo which can be used on the sign but is not compulsory.

I have also attached a photo of the front of our salon and the sign will be where I have outlined in yellow.

The size of the sign will be 119cm wide and 170cm high.

I am open to any nice classy design you can think of.

```html
<!DOCTYPE html>
<html lang="en">
<head>
<meta charset="UTF-8">
<title>Aurelia Nails – Window Sign</title>
<link href="https://fonts.googleapis.com/css2?family=Great+Vibes&family=Cinzel:wght@500;700&display=swap" rel="stylesheet">
<style>
  :root {
    --paper: #fbfcfd;
    --sky: #bfe3f2;
    --sky-deep: #6fb7d8;
    --teal: #9fd4e6;
    --rose: #e23f86;
    --gold: #a9823b;
    --gold-dark: #7d5e23;
    --skin-light: #f1d2c0;
    --skin-mid: #dcab92;
    --nail-pink: #ef4f8f;
  }
  * { margin: 0; padding: 0; box-sizing: border-box; }
  html, body { width: 720px; height: 1200px; overflow: hidden; background: var(--paper); }
  .sign {
    position: relative;
    width: 720px;
    height: 1200px;
    overflow: hidden;
    background: var(--paper);
  }
  .swooshes {
    position: absolute;
    top: 0; left: 0;
    width: 720px; height: 600px;
  }
  .brand {
    position: absolute;
    top: 90px; left: 0; right: 0;
    text-align: center;
    font-family: "Great Vibes", cursive;
    font-size: 112px;
    line-height: 1;
    color: var(--rose);
  }
  .hands-photo {
    position: absolute;
    left: 0; top: 300px;
    width: 500px; height: 900px;
    background:
      radial-gradient(ellipse at 40% 35%, rgba(239,79,143,0.35), transparent 45%),
      radial-gradient(ellipse at 30% 70%, rgba(239,79,143,0.25), transparent 40%),
      linear-gradient(160deg, var(--skin-light) 0%, var(--skin-mid) 70%, #c98f78 100%);
    border-top-right-radius: 60px;
  }
  .services {
    position: absolute;
    left: 500px; top: 560px;
    width: 210px;
  }
  .services__title {
    font-family: "Great Vibes", cursive;
    font-size: 62px;
    color: var(--gold);
    line-height: 1;
    margin-bottom: 18px;
  }
  .services__list { list-style: none; }
  .services__item {
    position: relative;
    padding-left: 20px;
    margin-bottom: 14px;
    font-family: "Cinzel", serif;
    font-weight: 700;
    font-size: 18px;
    line-height: 1.15;
    color: var(--gold-dark);
  }
  .services__item::before {
    content: "";
    position: absolute;
    left: 0; top: 6px;
    width: 8px; height: 8px;
    border-radius: 50%;
    background: var(--rose);
  }
  .gallery {
    position: absolute;
    left: 330px; top: 1040px;
    display: flex;
    gap: 14px;
  }
  .gallery__item {
    width: 114px; height: 114px;
    border-radius: 50%;
    border: 4px solid var(--gold);
  }
  .gallery__item--one { background: radial-gradient(circle at 45% 45%, var(--nail-pink), #8b3a4a 75%); }
  .gallery__item--two { background: radial-gradient(circle at 50% 50%, #e3a66c, #8c5a34 75%); }
  .gallery__item--three { background: radial-gradient(circle at 50% 50%, #d8b89a, #6b4a3a 75%); }
</style>
</head>
<body>
<main class="sign">
  <svg class="swooshes" viewBox="0 0 720 600" aria-hidden="true">
    <path d="M0 40 C200 120 420 0 720 60 L720 0 L0 0 Z" fill="var(--sky)" opacity="0.6"/>
    <path d="M0 250 C180 200 420 330 720 230 L720 300 C460 390 200 260 0 320 Z" fill="var(--teal)" opacity="0.55"/>
    <path d="M0 290 C220 240 460 360 720 280" stroke="var(--sky-deep)" stroke-width="3" fill="none" opacity="0.7"/>
    <path d="M300 600 C420 480 560 430 720 440 L720 520 C580 520 450 560 360 600 Z" fill="var(--sky)" opacity="0.5"/>
  </svg>

  <h1 class="brand">Aurelia Nails</h1>

  <div class="hands-photo" role="img" aria-label="Close-up photo of two hands with long pink and patterned manicured nails"></div>

  <section class="services">
    <h2 class="services__title">Services</h2>
    <ul class="services__list">
      <li class="services__item">Manicures</li>
      <li class="services__item">Pedicures</li>
      <li class="services__item">Velora Gel Builder</li>
      <li class="services__item">Acrylic Nails</li>
      <li class="services__item">KVT</li>
      <li class="services__item">Brenlux</li>
      <li class="services__item">Gel Polish</li>
    </ul>
  </section>

  <div class="gallery">
    <div class="gallery__item gallery__item--one" role="img" aria-label="Round photo of pink decorated nails"></div>
    <div class="gallery__item gallery__item--two" role="img" aria-label="Round photo of a pedicure"></div>
    <div class="gallery__item gallery__item--three" role="img" aria-label="Round photo of patterned nail art"></div>
  </div>
</main>
</body>
</html>
```